A Brochure to sell LED Downlights to clients

I am starting a campaign on google for LED down lights the link to the landing page can be found at brimfield.com.au/led .

When the client send a contact request i want to be able to send back a brochure of a picture of each light (Approx 6 - 8 types) and have a few sentences on each light and price brake down.

'Parvane Oslira 9w LED'

**Information**

1-10 lights $49
11-20 lights $45
21 - 40 lights $42
40 and over $40

EACH LIGHT:

Hi,

This is very good.

I
But,

Each light will have its own price.

Can i get it made like this;

Picture - Spec - Pricing in a table style please? - i like the layout it just need to suit the tables under:

picture - Brand - Price 1-10
Model - Price 11-20
Watts - Price 21-21
lumen - price 30- 40
Warranty = price 40+

Model - Price 11-20
Watts - Price 21-21
lumen - price 30- 40
Warranty = price 40+

Model - Price 11-20
Watts - Price 21-21
lumen - price 30- 40
Warranty = price 40+

and so on....

I want it to be on Microsoft Word so i can easily chop and edit the prices and images also. (So i can print to PDF)

For more information see my website to seek inspiration. I have a zip file of my logo for actual creation and should be also to source pictures of the lights when finalising the design.

brimfield.com.au

Thanks

Added 2 x additional Dimmers please see zip file, same layout/pricing as the downlights

Target Market(s)

Homeowners/commercial business owners

Industry/Entity Type

Electric Company

Font styles to use
Sans Serif

Colors
86cfc6
ffffff
000000

Requirements
Must have
• Professional looking, Colours to the theme of my logo/website
Nice to have
• An awesome design that sells it's self!!!!!!!
• My Logo font is 'Radikil" it would be nice to follow that theme if it doesn't look good i am open to have a nice legible font for the copy.
Should not have
• Cheesy light globes or images

```html
<!DOCTYPE html>
<html lang="en">
<head>
<meta charset="utf-8">
<title>Brimfield Electrical – LED Downlights Brochure</title>
<link href="https://fonts.googleapis.com/css2?family=Montserrat:wght@400;600;700&family=Questrial&display=swap" rel="stylesheet">
<style>
  :root {
    --teal: #0fa89b;
    --teal-soft: #86cfc6;
    --charcoal: #3d3d3d;
    --ink: #111111;
    --paper: #ffffff;
    --backdrop: #dcdcdc;
    --grid: #1aa89c;
  }
  * { margin: 0; padding: 0; box-sizing: border-box; }
  html, body { width: 1200px; height: 2980px; overflow: hidden; }
  body { background: var(--backdrop); font-family: "Questrial", sans-serif; position: relative; }

  .page { position: absolute; background: var(--paper); box-shadow: 6px 8px 12px rgba(0,0,0,.35); overflow: hidden; }

  /* Cover */
  .cover { left: 290px; top: 115px; width: 622px; height: 879px; }
  .cover__photo { position: absolute; left: 0; top: 0; width: 100%; height: 690px;
    background: linear-gradient(180deg, #ffffff 0%, #fbf8f2 22%, #e8dcc8 45%, #d4c2a4 62%, #8c7a62 85%, #5a4f44 100%); }
  .cover__title { position: absolute; top: 160px; left: 0; width: 100%; text-align: center; font-family: "Montserrat", sans-serif; font-weight: 700; font-size: 66px; letter-spacing: 2px; color: var(--teal); line-height: 1; }
  .cover__subtitle { position: absolute; top: 229px; left: 157px; width: 308px; height: 63px; border: 2px solid #555; text-align: center; font-family: "Montserrat", sans-serif; font-weight: 400; font-size: 54px; line-height: 58px; color: #333; background: rgba(255,255,255,.6); }
  .cover__stripe { position: absolute; left: 0; top: 690px; width: 100%; height: 12px; background: var(--teal); }
  .cover__band { position: absolute; left: 0; top: 702px; width: 100%; height: 177px; background: var(--charcoal); }

  .brand { position: absolute; display: flex; align-items: center; gap: 12px; font-family: "Questrial", sans-serif; color: var(--paper); }
  .brand__mark { width: 22px; height: 22px; background: var(--teal-soft); }
  .brand__name { font-size: 40px; line-height: 1; }
  .cover .brand { left: 24px; top: 812px; }
  .url { position: absolute; font-family: "Montserrat", sans-serif; font-weight: 600; color: var(--paper); }
  .cover .url { right: 24px; top: 840px; font-size: 20px; }

  /* Price sheet */
  .sheet { left: 294px; top: 1069px; width: 640px; height: 904px;
    background: linear-gradient(180deg, #f4f4f4 0%, #eeeeee 60%, #ffffff 80%); }
  .sheet__title { position: absolute; top: 36px; left: 0; width: 100%; text-align: center; font-family: "Montserrat", sans-serif; font-weight: 700; font-size: 26px; color: var(--teal); letter-spacing: .5px; }
  .spec-table { position: absolute; left: 40px; top: 81px; width: 556px; border: 2px solid var(--grid); border-radius: 22px; overflow: hidden; background: var(--paper); border-collapse: separate; border-spacing: 0; }
  .spec-table td { width: 111px; border-right: 1.5px solid var(--grid); border-bottom: 1.5px solid var(--grid); text-align: center; font-size: 13px; color: var(--ink); height: 75px; }
  .spec-table td:last-child { border-right: none; }
  .spec-table tr:last-child td { border-bottom: none; height: 103px; vertical-align: top; padding-top: 30px; }
  .spec-table .photo-row td { height: 124px; }
  .product-shot { display: block; width: 70px; height: 70px; margin: 0 auto; border-radius: 50%; background: radial-gradient(circle, #ffffff 30%, #c9c9c9 60%, #6d6d6d 100%); }
  .product-shot--driver { border-radius: 6px; background: linear-gradient(160deg, #3d5fae, #1f3470); width: 44px; height: 56px; }

  .tier-tab { position: absolute; left: 193px; top: 733px; width: 254px; height: 28px; background: var(--teal); color: var(--paper); text-align: center; font-size: 17px; line-height: 28px; }
  .tier-panel { position: absolute; left: 28px; top: 761px; width: 590px; height: 95px; background: var(--charcoal); border: 3px solid var(--teal); border-radius: 22px; color: var(--paper); font-size: 20px; }
  .tier { position: absolute; }
  .tier b { font-weight: 400; color: var(--teal-soft); }
  .tier--a { left: 36px; top: 14px; } .tier--b { left: 36px; top: 46px; }
  .tier--c { left: 360px; top: 14px; } .tier--d { left: 360px; top: 46px; }
  .sheet .url { right: 22px; top: 866px; font-size: 14px; font-weight: 400; color: #444; font-family: "Questrial", sans-serif; }

  /* Back cover */
  .back { left: 290px; top: 2025px; width: 622px; height: 876px; background: var(--teal); }
  .back__bar { position: absolute; left: 0; top: 0; width: 100%; height: 14px; background: #6b6b6b; }
  .back__photo { position: absolute; left: 0; top: 14px; width: 100%; height: 862px;
    background: radial-gradient(ellipse at 35% 60%, rgba(0,60,55,.28), transparent 60%), linear-gradient(180deg, #14ada0 0%, #0b9c90 45%, #0a8f84 70%, #0fa89b 100%); }
  .back .brand { left: 0; width: 100%; top: 312px; justify-content: center; }
  .back .url { left: 0; width: 100%; text-align: center; top: 820px; font-size: 22px; }
</style>
</head>
<body>

<section class="page cover">
  <div class="cover__photo" role="img" aria-label="Photo of a retail shop interior lit by recessed LED downlights"></div>
  <h1 class="cover__title">PRODUCT</h1>
  <div class="cover__subtitle">CATALOG</div>
  <div class="cover__stripe"></div>
  <div class="cover__band"></div>
  <div class="brand"><span class="brand__mark"></span><span class="brand__name">brimfield Electrical</span></div>
  <div class="url">brimfield.com.au</div>
</section>

<section class="page sheet">
  <h2 class="sheet__title">CHOOSE YOUR STYLE OF LED DOWNLIGHTS</h2>
  <table class="spec-table">
    <tr class="photo-row">
      <td><span class="product-shot" role="img" aria-label="Product photo of a white LED downlight"></span></td>
      <td><span class="product-shot" role="img" aria-label="Product photo of a white LED downlight with driver"></span></td>
      <td><span class="product-shot" role="img" aria-label="Product photo of a black gimbal LED downlight"></span></td>
      <td><span class="product-shot" role="img" aria-label="Product photo of a satin chrome LED downlight"></span></td>
      <td><span class="product-shot product-shot--driver" role="img" aria-label="Product photo of an LED driver"></span></td>
    </tr>
    <tr><td>Brand</td><td>Brand</td><td>Brand</td><td>Brand</td><td>Brand</td></tr>
    <tr><td>Model</td><td>Model</td><td>Model</td><td>Model</td><td>Model</td></tr>
    <tr><td>Watts</td><td>Watts</td><td>Watts</td><td>Watts</td><td>Watts</td></tr>
    <tr><td>lumen</td><td>lumen</td><td>lumen</td><td>lumen</td><td>lumen</td></tr>
    <tr><td>Warranty</td><td>Warranty</td><td>Warranty</td><td>Warranty</td><td>Warranty</td></tr>
    <tr><td>Price</td><td>Price</td><td>Price</td><td>Price</td><td>Price</td></tr>
  </table>
  <div class="tier-tab">Parvane Oslira 9w LED</div>
  <div class="tier-panel">
    <div class="tier tier--a">1-10......lights : <b>$49</b></div>
    <div class="tier tier--b">11-20...lights : <b>$45</b></div>
    <div class="tier tier--c">21-40...lights : <b>$42</b></div>
    <div class="tier tier--d">40 and over : <b>$40</b></div>
  </div>
  <div class="url">www.brimfield.com.au</div>
</section>

<section class="page back">
  <div class="back__bar"></div>
  <div class="back__photo" role="img" aria-label="Teal-toned photo of a bedroom lit by downlights"></div>
  <div class="brand"><span class="brand__mark"></span><span class="brand__name">brimfield Electrical</span></div>
  <div class="url">www.brimfield.com.au</div>
</section>

</body>
</html>
```